Welbourne Dental, P.C. New stationary and business card for modern Dental Office

We need a new stationary/envelope/business card design using our newly designed logo. We are looking for an upscale look. Our new logo is used on our signage, using black as the background and white for the lettering. We would like the stationary to have black, white, possible greys or silver. We are looking for a letterhead, envelope, and business card design for three different employees, as well as a 4th card, same design, but just general with no employee name.

Project Deadline Extended
Reason: We began this project in the middle of our move into our new office. Things got pretty hectic and we just didn't have the time to go through designs. We now settled in and finally eliminated the designs that didn't work for us. We would like to extend the project another 5 days, and then finalize our decision. Most of the submissions showed business cards alone, with no stationary designs. Our original request was for stationary and business cards. Please keep this in mind.

Target Market(s)

Dental patients expecting high quality, cosmetic dentistry

Industry/Entity Type

Business

Contact Information for Business Card

Will need a design using our logo. All cards will be the same, other than that one card will have Office Managers name, One for the Doctor, Hygienist,
1. Office Manager - Marisol Dubrovka
2. Hygienist - Kayleigh Morrow
3. Gordon T. Welbourne, D.D.S.
4. One general one with no staff names

Font styles to use
Other font styles liked:
• see upload

Colors
000000
1b1b1b
757575
c9c9c9
e8e8e8
ffffff

Requirements
Must have
• -Logo
• -Phone number (718)555-0193
• -Address: 4352 63rd Ave
• Lower Level
• Brooklyn, NY 11290

```html
<!DOCTYPE html>
<html lang="en">
<head>
<meta charset="utf-8">
<title>Welbourne Dental, P.C. — Business Card</title>
<link rel="stylesheet" href="https://fonts.googleapis.com/css2?family=Marcellus&family=Tenor+Sans&display=swap">
<style>
  :root {
    --black: #000000;
    --ink: #1b1b1b;
    --grey: #757575;
    --silver: #c9c9c9;
    --mist: #e8e8e8;
    --white: #ffffff;
    --bronze: #8a7a6a;
    --backdrop: #d9d6d2;
  }
  * { margin: 0; padding: 0; box-sizing: border-box; }
  html, body { width: 1200px; height: 969px; overflow: hidden; }
  body { background: var(--backdrop); position: relative; }

  .business-card {
    position: absolute;
    left: 100px; top: 200px;
    width: 1000px; height: 568px;
    background: var(--black);
    border-radius: 40px;
    overflow: hidden;
    box-shadow: 0 18px 40px rgba(0,0,0,0.25);
  }
  .silver-band {
    position: absolute;
    left: 560px; top: 86px;
    width: 440px; height: 388px;
    background: linear-gradient(90deg, var(--black) 0%, #4a4644 30%, #a9a29b 60%, var(--silver) 80%, #9b958f 100%);
  }
  .emblem-ring {
    position: absolute;
    left: 0; top: 0;
    width: 1000px; height: 568px;
  }
  .practice-name {
    position: absolute;
    left: 697px; top: 284px;
    width: 290px;
    transform: translate(-50%, -50%);
    font-family: "Marcellus", serif;
    font-size: 25px;
    line-height: 1;
    text-align: center;
    color: var(--silver);
    white-space: nowrap;
  }

  .staff-name {
    position: absolute;
    left: 60px; top: 112px;
    font-family: "Marcellus", serif;
    font-size: 34px;
    font-weight: 400;
    letter-spacing: 1px;
    text-transform: uppercase;
    color: var(--bronze);
  }
  .staff-title {
    position: absolute;
    left: 60px; top: 162px;
    font-family: "Tenor Sans", sans-serif;
    font-size: 25px;
    color: var(--mist);
  }
  .address {
    position: absolute;
    left: 60px; top: 218px;
    font-family: "Tenor Sans", sans-serif;
    font-size: 25px;
    line-height: 37px;
    color: var(--mist);
    font-style: normal;
  }
  .contact-list {
    position: absolute;
    left: 60px; top: 346px;
    list-style: none;
    font-family: "Tenor Sans", sans-serif;
    font-size: 25px;
    line-height: 38px;
    color: var(--silver);
  }
  .contact-list li { display: flex; align-items: center; gap: 14px; }
  .contact-icon { width: 20px; height: 20px; fill: var(--grey); flex: none; }
</style>
</head>
<body>
  <article class="business-card">
    <div class="silver-band"></div>
    <svg class="emblem-ring" viewBox="0 0 1000 568" aria-hidden="true">
      <circle cx="697" cy="284" r="172" fill="var(--black)" stroke="#b8b1aa" stroke-width="5"/>
    </svg>
    <p class="practice-name">Welbourne Dental, P.C.</p>

    <h1 class="staff-name">Julian Serrano</h1>
    <p class="staff-title">CEO/FOUNDER</p>
    <address class="address">
      4352 63rd Ave<br>
      Lower Level<br>
      Brooklyn, NY 11290
    </address>
    <ul class="contact-list">
      <li>
        <svg class="contact-icon" viewBox="0 0 24 24"><path d="M6.6 10.8a15.1 15.1 0 0 0 6.6 6.6l2.2-2.2a1 1 0 0 1 1-.25 11.4 11.4 0 0 0 3.6.57 1 1 0 0 1 1 1V20a1 1 0 0 1-1 1A17 17 0 0 1 3 4a1 1 0 0 1 1-1h3.5a1 1 0 0 1 1 1c0 1.25.2 2.450.57 3.57a1 1 0 0 1-.25 1z"/></svg>
        (718)555-0193
      </li>
      <li>
        <svg class="contact-icon" viewBox="0 0 24 24"><path d="M2 5h20v14H2z M4 7v.5l8 5 8-5V7l-8 5z" fill-rule="evenodd"/></svg>
        info@welbournedental.com
      </li>
      <li>
        <svg class="contact-icon" viewBox="0 0 24 24"><path d="M12 2a10 10 0 1 0 0 20 10 10 0 0 0 0-20zm6.9 9h-3a15 15 0 0 0-1.3-5.6A8 8 0 0 1 18.9 11zM12 4.1c.9 1.2 1.7 3.6 1.9 6.9h-3.8c.2-3.3 1-5.7 1.9-6.9zM9.4 5.4A15 15 0 0 0 8.1 11h-3a8 8 0 0 1 4.3-5.6zM5.1 13h3a15 15 0 0 0 1.3 5.6A8 8 0 0 1 5.1 13zm6.9 6.9c-.9-1.2-1.7-3.6-1.9-6.9h3.8c-.2 3.3-1 5.7-1.9 6.9zm2.6-1.3a15 15 0 0 0 1.3-5.6h3a8 8 0 0 1-4.3 5.6z"/></svg>
        www.welbournedental.com
      </li>
    </ul>
  </article>
</body>
</html>
```